Etiketten für Kosmetik Produkte  100% Natural Made in Germany
Etiketten für Kosmetik Produkte 100% Natural Made in Germany
Zielgruppe
auf Hochwertige -zertifizierte Naturprodukte wert legen.
Hergestellt in Deutschland und Verpackt
Aufgabenstellung
Hallo ihr lieben,
für die SilbTau Kosmetik - wünschen wir einen neuen frischen Style - das dunkle Etikett möchten wir los werden.
Ein helles frisches Design
Zielgruppe- alle die auf Hochwertige - zertifizierte Naturprodukte bevorzugen
Die Produkte haben mit eine VERUN Zertifizierung - Höchste Qalität an Naturprodukte
Das Glas was wir nutzen ist ein violettes Glas und sehr hochwertig was wir beibehalten möchten.
Das Produkt ist dadurch sehr Geschütz und nachhaltig dazu
Es sind 12 Produkte - Design bleibt bei allen gleich.
Design Wunsch -!!!!
Was gut zum Glas Passt- nur kein schwarz bitte
und Produkt gut passt
Weiß - Kupfer eventuell
Kein Muss - sind für alles offen ( nur kein schwarz
Logo - Name bleibt :-)
Das Design von Tesoro Naturkosmetik
Gefällt uns sehr gut in der Richtung
Was die Natürlichkeit- Reinheit - Qualität
Verkörpert:-)
Fotos zum Prosukt:
Hier ein link zum Instagram
https://instagram.com/lumaroze.spain?igshid=MzRlODBiNWFlZA==
https://instagram.com/silbtau_naturkosmetik?igshid=MzRlODBiNWFlZA==
An den Flyer den wir hochgeladen kann man sehen um welche Produkte es sich handelt und auch im Instagram zu sehen sind.
Wenn ihr weitere Fotos benötigen tut- bitte melden
Viel Glück :-) danke für eure Unterstützung

```html
<!DOCTYPE html>
<html lang="de">
<head>
<meta charset="utf-8">
<title>SilbTau Naturkosmetik – Lemon &amp; Orange Etikett</title>
<link rel="stylesheet" href="https://fonts.googleapis.com/css2?family=Cinzel:wght@400&family=Pinyon+Script&family=Montserrat:wght@400;600&display=swap">
<style>
  :root {
    --canvas-bg: #ffffff;
    --label-bg: #f1f0ee;
    --label-edge: #e4e2de;
    --gold: #c6a46a;
    --gold-light: #e8c96a;
    --gold-deep: #b8892a;
    --ink-grey: #5e5e5e;
  }
  * { margin: 0; padding: 0; box-sizing: border-box; }
  html, body {
    width: 1200px;
    height: 960px;
    overflow: hidden;
    background: var(--canvas-bg);
  }
  .canvas {
    position: relative;
    width: 1200px;
    height: 960px;
  }
  .label {
    position: absolute;
    left: 190px;
    top: 70px;
    width: 820px;
    height: 820px;
    border-radius: 50%;
    background: var(--label-bg);
    box-shadow: inset 0 0 0 2px var(--label-edge);
    overflow: hidden;
  }
  .label__veins {
    position: absolute;
    inset: 0;
    width: 100%;
    height: 100%;
  }
  .brand {
    position: absolute;
    top: 95px;
    left: 0;
    right: 0;
    text-align: center;
    color: var(--gold);
    font-family: "Cinzel", serif;
    font-weight: 400;
  }
  .brand__mark {
    display: block;
    width: 54px;
    height: 54px;
    margin: 0 auto 18px;
    border: 2px solid var(--gold);
    border-radius: 50%;
  }
  .brand__name {
    display: block;
    font-size: 46px;
    letter-spacing: 1px;
    line-height: 1;
  }
  .brand__sub {
    display: block;
    margin-top: 6px;
    font-size: 21px;
    letter-spacing: 1px;
    line-height: 1;
  }
  .product-name {
    position: absolute;
    top: 310px;
    left: 0;
    right: 0;
    text-align: center;
    color: var(--gold);
    font-family: "Pinyon Script", cursive;
    font-weight: 400;
    font-size: 118px;
    line-height: 0.98;
  }
  .product-name__line { display: block; }
  .product-name__line--first { padding-left: 40px; }
  .product-name__line--second { padding-left: 20px; }
  .product-line {
    position: absolute;
    top: 620px;
    left: 0;
    right: 0;
    display: flex;
    justify-content: center;
    align-items: center;
    gap: 14px;
    font-family: "Montserrat", sans-serif;
    font-size: 24px;
    color: var(--ink-grey);
    letter-spacing: 0.5px;
  }
  .product-line__category { font-weight: 600; }
  .product-line__divider {
    width: 1px;
    height: 40px;
    background: var(--ink-grey);
    transform: rotate(12deg);
  }
  .product-line__quality { font-weight: 400; }
</style>
</head>
<body>
<main class="canvas">
  <section class="label">
    <svg class="label__veins" viewBox="0 0 820 820" role="img" aria-label="Goldene Marmoradern als Dekor entlang des Etikettenrands">
      <defs>
        <radialGradient id="veinGlow" cx="50%" cy="50%" r="50%">
          <stop offset="78%" stop-color="#e8c96a" stop-opacity="0"/>
          <stop offset="94%" stop-color="#d9b65a" stop-opacity="0.35"/>
          <stop offset="100%" stop-color="#c6a46a" stop-opacity="0.55"/>
        </radialGradient>
      </defs>
      <circle cx="410" cy="410" r="410" fill="url(#veinGlow)"/>
    </svg>

    <div class="brand">
      <span class="brand__mark"></span>
      <span class="brand__name">SILBTAU</span>
      <span class="brand__sub">NATURKOSMETIK</span>
    </div>

    <h1 class="product-name">
      <span class="product-name__line product-name__line--first">Lemon</span>
      <span class="product-name__line product-name__line--second">&amp; Orange</span>
    </h1>

    <p class="product-line">
      <span class="product-line__category">BODY CARE</span>
      <span class="product-line__divider"></span>
      <span class="product-line__quality">ORGANIC</span>
    </p>
  </section>
</main>
</body>
</html>
```